Grey orchard secret

UPDATED BRIEF:
I'm just updating the brief to enable any new submissions to come up with their own ideas. I have tried to offer my ideas below, but I am too close to the project therefor any new submissions are probably best using your talent. The main thing is it stands out and someone would want to buy it against the competition. All submissions have been excellent, so to be fair I will put the winning vote to family and friends. I am too close and biased to make the final choice.
This book is part memoire/ part biography/ part diary/ part self help.
My world is falling apart. I use the analogy of being lost at see. This book is my ships log. It could be a torn out PAGE of the log, a POSTER, or A MESSAGE a bottle.
It needs to be clear in the title, so GREY ORCHARD SECRET needs to stand out. BOO could be a wax seal, like a stamp. 'You've found the' and 'We're dancing at dusk' are less important. The title is: BOO You've found the GREY ORCHARD SECRET We're dancing at dusk.
Other subliminal random words are: family, paranoia, sex addiction, depression, marriage, divorce.
The other idea is flame red. Needs to be subtle to show my life is going up in flames. The diary page/poster/note should be singed or worn.
Ideally text font should be bespoke. Whether some or all are slightly wonky to show that my life is falling apart.
Octopus bottom left with tentacles spread over spine is a firm favourite
Text on spine needs to be large to stand out. Open to suggestions but nothing over simple.Good luck

Target Market(s)

30-60 years

Colors

Requirements
Must have
• Book size. I'm assuming: 21.5cm x 13.5cm x 2.5cm. I will need ebook version and paperback version. ISBN details will follow later

```html
<!DOCTYPE html>
<html lang="en">
<head>
<meta charset="utf-8">
<title>Grey Orchard Secret – Cover Spread</title>
<link rel="stylesheet" href="https://fonts.googleapis.com/css2?family=Anton&family=Bebas+Neue&family=EB+Garamond:wght@400&display=swap">
<style>
  :root {
    --page-bg: #f1f1f1;
    --red-bright: #ee2a35;
    --red-deep: #a80f18;
    --spine-red: #dc1f2a;
    --panel-white: #ffffff;
    --panel-edge: #dedede;
    --ink: #111111;
    --ink-soft: #3a3a3a;
    --paper: #ffffff;
    --sign-red: #e3111b;
  }
  * { margin: 0; padding: 0; box-sizing: border-box; }
  html, body { width: 899px; height: 1200px; overflow: hidden; }
  body { background: var(--page-bg); position: relative; }

  .spread-frame {
    position: absolute; left: 20px; top: 303px;
    width: 1096px; height: 758px;
    transform: scale(0.784); transform-origin: top left;
    display: flex;
    box-shadow: 0 10px 30px rgba(0,0,0,.18);
  }

  .back-cover, .front-cover {
    position: relative; width: 505px; height: 100%;
    background: radial-gradient(ellipse at 55% 50%, var(--red-bright) 0%, #dd1e29 55%, var(--red-deep) 100%);
  }
  .spine {
    position: relative; width: 86px; height: 100%;
    background: linear-gradient(90deg, #c51a24, var(--spine-red) 30%, var(--spine-red) 70%, #c51a24);
    border-left: 1px solid rgba(0,0,0,.12);
    border-right: 1px solid rgba(0,0,0,.12);
  }

  .warning-sign { position: absolute; display: block; }
  .back-cover .warning-sign { left: 200px; top: 32px; width: 108px; height: 92px; }

  .blurb {
    position: absolute; left: 40px; width: 428px;
    font-family: "EB Garamond", serif; font-size: 16.4px; line-height: 19.6px;
    color: var(--paper); text-align: justify;
  }
  .blurb p + p { margin: 0; }
  .blurb-hook { top: 142px; }
  .blurb-summary { top: 378px; }

  .isbn-box {
    position: absolute; left: 326px; top: 632px; width: 136px; height: 84px;
    background: var(--paper);
  }

  .spine-text {
    position: absolute; top: 42px; left: 50%;
    transform: translateX(-50%);
    writing-mode: vertical-rl;
    color: var(--paper); white-space: nowrap;
    display: flex; align-items: center;
  }
  .spine-title { font-family: "Anton", sans-serif; font-size: 30px; letter-spacing: .5px; line-height: 1; }
  .spine-subtitle { font-family: "Bebas Neue", sans-serif; font-size: 20px; letter-spacing: 4px; margin-top: 30px; line-height: 1; }

  .series-line {
    position: absolute; top: 22px; left: 0; width: 100%; text-align: center;
    font-family: "Bebas Neue", sans-serif; font-size: 46px; letter-spacing: 1.5px;
    color: var(--paper); line-height: 1;
  }

  .title-panel {
    position: absolute; left: 47px; top: 74px; width: 410px; height: 592px;
    background: radial-gradient(ellipse at 50% 45%, var(--panel-white) 55%, var(--panel-edge) 100%);
    text-align: center;
  }
  .title-lead {
    margin-top: 26px;
    font-family: "Bebas Neue", sans-serif; font-size: 50px; line-height: 1;
    color: var(--ink); letter-spacing: 1px;
  }
  .title-lead .title-seal { color: var(--ink-soft); }
  .title-main {
    font-family: "Anton", sans-serif; color: var(--ink);
    line-height: .98; margin-top: 6px;
  }
  .title-main .line-a { display: block; font-size: 74px; letter-spacing: 1px; }
  .title-main .line-b { display: block; font-size: 108px; letter-spacing: 2px; }
  .title-tail {
    font-family: "Bebas Neue", sans-serif; font-size: 48px; line-height: 1;
    color: var(--ink); margin-top: 8px; letter-spacing: 1px;
  }
  .title-panel .warning-sign { left: 103px; top: 386px; width: 206px; height: 176px; }

  .author-name {
    position: absolute; top: 688px; left: 0; width: 100%; text-align: center;
    font-family: "Bebas Neue", sans-serif; font-size: 50px; letter-spacing: 17px;
    color: var(--paper); line-height: 1; padding-left: 17px;
  }
</style>
</head>
<body>
  <div class="spread-frame">
    <section class="back-cover">
      <svg class="warning-sign" viewBox="0 0 120 102" aria-hidden="true">
        <path d="M60 8 L112 94 L8 94 Z" fill="var(--paper)" stroke="var(--sign-red)" stroke-width="12" stroke-linejoin="round"/>
        <path d="M55 36 h10 l-2 32 h-6 z" fill="var(--ink)"/>
        <circle cx="60" cy="79" r="5.5" fill="var(--ink)"/>
      </svg>
      <div class="blurb blurb-hook">
        <p>So you’ve found your career, got married, bought your home. Life is great, you are happy and everything just seems to fit into place.</p>
        <p>Then all of a sudden your perfect Utopia starts to fall apart. The life that was once full of promise, hope, and ambition, is now starting to fall apart. You’ve reached the summit and the panoramic view is not what you expected! The storm approaches and you panic. Worry, fear, and distress fill your mind. Congratulations you have reached the Nirvana of a GOS!</p>
      </div>
      <div class="blurb blurb-summary">
        <p>This book is an honest reflection of life according to a dreamer. Somebody who’s lost his way. A person who has it all, yet, has nothing. Someone who has lost his place in society, has so much to give, yet feels so empty and hopeless inside. A story of living life with depression. The highs and lows of a family man just trying to make it in life. The ultimate guide to a fragile mind in Grey orchard secret fighting: Sex addiction, Periods, the menopause,</p>
        <p>Marriage conflict, Parenting, finance, Divorce, and Affairs</p>
      </div>
      <div class="isbn-box"></div>
    </section>

    <section class="spine">
      <div class="spine-text">
        <span class="spine-title">BOO! GREY ORCHARD SECRET</span>
        <span class="spine-subtitle">WE'RE DANCING AT DUSK</span>
      </div>
    </section>

    <section class="front-cover">
      <div class="series-line">THE NUMBER ONE BESTDAD</div>
      <div class="title-panel">
        <h1 class="book-title">
          <div class="title-lead"><span class="title-seal">BOO</span> YOU'VE FOUND THE</div>
          <div class="title-main"><span class="line-a">GREY ORCHARD</span><span class="line-b">SECRET</span></div>
          <div class="title-tail">WE'RE DANCING AT DUSK</div>
        </h1>
        <svg class="warning-sign" viewBox="0 0 120 102" aria-hidden="true">
          <path d="M60 8 L112 94 L8 94 Z" fill="var(--paper)" stroke="var(--sign-red)" stroke-width="11" stroke-linejoin="round"/>
          <path d="M55.5 34 h9 l-2 34 h-5 z" fill="var(--ink)"/>
          <circle cx="60" cy="79" r="5" fill="var(--ink)"/>
        </svg>
      </div>
      <div class="author-name">MARTIN HALE</div>
    </section>
  </div>
</body>
</html>
```